Bref créative
Keystone Assurance
Information security and compliance
Information Technology
keystoneassurance.example
We are an information technology company that specializes in auditing information security for merchants, retailers, and services providers that take credit cards and process payment transactions. We are a professional services business in information security.
Keystone Assurance should convey that we work to leverage a client’s existing systems and abilities to meet current compliance requirements. We want to convey that we will create a symbiotic relationship between organizations and compliance regulations. Symbiotic in this case bringing together two dissimilar organisms (companies) in close union with similar purpose.
Like: Clean, concise, smart. what I need.
Dislike: busy, cool, trendy cheap, template.
left side
https://www.ferrolock.example/
http://us.quorvanet.example/us/home/
http://www.brimstackgroup.example/default.html
I want to be able to update the content easily and have some type of streaming infosec related news. I want a contact page form what emails me the costumer questions/info and list my phone and email in a graphic that cannot be read by scan engines..
Tabs need to be: Home, Solutions, Industries, Contact Us. All tabs except home have options that open additional pages.
I want a clear clean font, one font type only. Colors are flexible to you artistic thoughts and my existing logo. My logo is in a few formats I like # 7 but can use different colors on other pages or formats.
I am not sure what "Nav placement" is so I selected the default. If you know better, just do it!
Logo in various formats and Styles. Some are suited for background and some color variations. Designers can be creative - I like #7 as a primary style but I am not married to that if you come up with a nice looking pages.
Continuation for log upload.
continuation of logo...

```html
<!DOCTYPE html>
<html lang="en">
<head>
<meta charset="utf-8">
<title>Keystone Assurance</title>
<link rel="stylesheet" href="https://fonts.googleapis.com/css2?family=Open+Sans:wght@400;600;700;800&display=swap">
<style>
:root{
  --green:#66b22a;
  --green-dark:#3f8a12;
  --green-light:#9bd34e;
  --teal:#17788a;
  --teal-dark:#0f5a68;
  --red:#c3161d;
  --red-dark:#8e0c10;
  --orange:#e0591a;
  --navy:#0d2944;
  --ink:#1e2b36;
  --grey:#5b646b;
  --page:#eef0f1;
  --card-border:#7fc8d6;
}
*{margin:0;padding:0;box-sizing:border-box}
html,body{width:1200px;height:989px;overflow:hidden;background:#fff}
body{font-family:"Open Sans",Arial,sans-serif;color:var(--ink)}
.page{position:relative;width:1200px;height:989px;background:var(--page);overflow:hidden}

/* header */
.header{position:absolute;left:0;top:0;width:1200px;height:155px;background:linear-gradient(180deg,#ffffff 0%,#f3f6f4 100%)}
.brand{position:absolute;left:28px;top:50px;display:flex;align-items:center;gap:18px}
.brand-mark{width:78px;height:78px;background:var(--green)}
.brand-name{font-size:46px;font-weight:700;color:var(--navy);letter-spacing:.5px}
.phone{position:absolute;right:28px;top:18px;display:flex;align-items:center;gap:10px;font-size:22px;font-weight:700;color:var(--ink)}
.social{position:absolute;right:28px;top:78px;display:flex;gap:10px}
.social span{width:38px;height:38px;border-radius:5px;background:#9aa4ab}

/* hero */
.hero{position:absolute;left:0;top:155px;width:1200px;height:353px;background:linear-gradient(180deg,var(--red) 0%,var(--red-dark) 100%)}
.hero-visual{position:absolute;left:0;top:0;width:760px;height:353px;background:radial-gradient(circle at 62% 50%,#4a5b2a 0%,#17230f 45%,#050805 100%)}
.hero-panel{position:absolute;left:760px;top:0;width:400px;height:353px;padding:46px 0 0 0;color:#fff}
.hero-title{font-size:38px;font-weight:800;letter-spacing:.3px;line-height:1}
.hero-sub{margin-top:26px;font-size:19px;font-weight:700;color:#ffb23a}
.hero-text{margin-top:6px;font-size:15px;font-weight:600;line-height:1.35;text-transform:uppercase;width:330px}
.btn-light{display:inline-block;margin-top:22px;padding:8px 16px;background:#fff;color:var(--ink);border-radius:6px;font-size:15px;font-weight:800;box-shadow:0 2px 4px rgba(0,0,0,.4)}
.hero-dots{position:absolute;left:800px;top:323px;display:flex;gap:8px}
.hero-dots span{width:12px;height:12px;border-radius:50%;background:#f0b7b9}
.hero-dots span.on{background:#fff}
.hero-next{position:absolute;right:6px;top:160px;color:#fff}

/* navigation */
.nav{position:absolute;left:21px;top:166px;width:322px;list-style:none}
.nav li{position:relative;height:72px;margin-bottom:4px;display:flex;align-items:center;background:linear-gradient(180deg,var(--green-light) 0%,var(--green) 55%,var(--green-dark) 100%);border-radius:0 6px 6px 0;color:#fff;font-size:20px;font-weight:700}
.nav li.active{background:linear-gradient(180deg,#b6e36a 0%,#79c531 60%,#4d9a18 100%)}
.nav-icon{width:82px;height:100%;display:flex;align-items:center;justify-content:center;background:rgba(0,0,0,.12);margin-right:24px}

/* news */
.news{position:absolute;left:21px;top:521px;width:260px}
.section-title{font-size:22px;font-weight:700;color:var(--ink);letter-spacing:.3px}
.news-list{list-style:none;margin-top:14px}
.news-item{display:flex;gap:10px;padding:10px 4px;border-top:1px solid #d5d9dc;background:#fff}
.news-item + .news-item{margin-top:8px}
.cal{flex:none;width:30px;height:30px;background:var(--green);border-radius:3px;position:relative}
.cal::after{content:"";position:absolute;left:4px;right:4px;bottom:4px;top:10px;background:#fff}
.news-date{font-size:14px;font-weight:600;color:var(--ink)}
.news-link{font-size:13px;color:var(--orange);text-decoration:underline}
.news-text{font-size:13px;color:var(--grey);line-height:1.35}
.more{display:block;text-align:right;margin-top:14px;font-size:13px;color:var(--red);text-decoration:underline}

/* services */
.services{position:absolute;left:299px;top:521px;width:877px}
.services .section-title{font-size:23px}
.service-bar{margin-top:10px;height:64px;border-radius:8px;background:linear-gradient(180deg,#2b98ab 0%,var(--teal) 50%,var(--teal-dark) 100%);display:flex}
.service-tab{flex:1;display:flex;align-items:center;gap:12px;padding-left:14px;color:#fff;font-size:24px;font-weight:700}
.num{width:42px;height:42px;border-radius:50%;background:#fff;color:var(--ink);display:flex;align-items:center;justify-content:center;font-size:24px;font-weight:800}
.cards{display:flex;justify-content:space-between;margin-top:10px;padding:0 8px}
.card{width:262px;height:292px;background:#fff;border:2px solid var(--card-border);border-radius:6px;padding:16px 18px}
.card-title{font-size:14px;font-weight:800;color:var(--ink)}
.card-text{margin-top:8px;font-size:13px;color:var(--grey);line-height:1.35}
.card-links{list-style:none;margin-top:10px}
.card-links li{font-size:13px;color:var(--orange);text-decoration:underline;line-height:1.55;padding-left:14px;position:relative}
.card-links li::before{content:"";position:absolute;left:0;top:7px;width:6px;height:6px;background:var(--orange)}
.btn-teal{display:inline-flex;align-items:center;gap:6px;margin-top:14px;padding:5px 12px;background:var(--teal);color:#fff;border-radius:4px;font-size:13px;font-weight:700}
.btn-teal i{width:12px;height:12px;border-radius:50%;background:#fff;display:inline-block}

/* footer */
.footer{position:absolute;left:0;top:941px;width:1200px;height:48px;background:var(--navy);color:#fff;font-size:14px;display:flex;align-items:center;justify-content:space-between;padding:0 28px}
.footer nav{display:flex;gap:10px}
</style>
</head>
<body>
<div class="page">

  <header class="header">
    <div class="brand">
      <span class="brand-mark"></span>
      <span class="brand-name">Keystone Assurance</span>
    </div>
    <div class="phone">
      <svg width="26" height="26" viewBox="0 0 24 24" aria-hidden="true"><path fill="#c3161d" d="M6.6 10.8a15.5 15.5 0 0 0 6.6 6.6l2.2-2.2c.3-.3.7-.4 1-.2 1.1.4 2.3.6 3.6.6.6 0 1 .4 1 1V20c0 .6-.4 1-1 1A17 17 0 0 1 3 4c0-.6.4-1 1-1h3.5c.6 0 1 .4 1 1 0 1.3.2 2.5.6 3.6.1.3 0 .7-.2 1z"/></svg>
      Toll Free 1-800-555-0142
    </div>
    <div class="social" aria-label="Social links">
      <span></span><span></span><span></span><span></span>
    </div>
  </header>

  <section class="hero">
    <div class="hero-visual" role="img" aria-label="Padlocked yellow folder in front of a dark field of green binary code"></div>
    <div class="hero-panel">
      <h1 class="hero-title">INFORMATION SECURITY</h1>
      <p class="hero-sub">FOR MERCHANTS</p>
      <p class="hero-text">Cum sociis natoque penatibus et magnisdis parturient montes, nascetur ridiculus mus.</p>
      <span class="btn-light">LEARN MORE ›</span>
    </div>
    <div class="hero-dots"><span class="on"></span><span></span><span></span><span></span></div>
    <svg class="hero-next" width="18" height="28" viewBox="0 0 18 28" aria-hidden="true"><path d="M4 4l10 10-10 10" fill="none" stroke="#fff" stroke-width="4"/></svg>
  </section>

  <ul class="nav">
    <li class="active"><span class="nav-icon"><svg width="34" height="30" viewBox="0 0 34 30" aria-hidden="true"><path d="M17 2 2 15h5v13h8v-8h4v8h8V15h5z" fill="#fff"/></svg></span>Home</li>
    <li><span class="nav-icon"><svg width="32" height="32" viewBox="0 0 32 32" aria-hidden="true"><circle cx="16" cy="16" r="10" fill="none" stroke="#fff" stroke-width="6" stroke-dasharray="5 3"/><circle cx="16" cy="16" r="4" fill="#fff"/></svg></span>Solutions</li>
    <li><span class="nav-icon"><svg width="30" height="32" viewBox="0 0 30 32" aria-hidden="true"><rect x="4" y="4" width="22" height="26" rx="2" fill="none" stroke="#fff" stroke-width="3"/><path d="M9 12h12M9 18h12M9 24h8" stroke="#fff" stroke-width="3"/></svg></span>Industries</li>
    <li><span class="nav-icon"><svg width="32" height="28" viewBox="0 0 32 28" aria-hidden="true"><path d="M4 3h24v16H14l-7 6v-6H4z" fill="#fff"/></svg></span>Contact Us</li>
  </ul>

  <aside class="news">
    <h2 class="section-title">NEWS &amp; EVENTS</h2>
    <ul class="news-list">
      <li class="news-item"><span class="cal"></span><div><p class="news-date">June 22, 2011</p><p class="news-link">Consectetuer adipiscing</p><p class="news-text">Sectetuer adipiscing aenean nonummy maurissellus.</p></div></li>
      <li class="news-item"><span class="cal"></span><div><p class="news-date">June 15, 2011</p><p class="news-link">Sociis natoque penatibus montes</p><p class="news-text">Aenean nonummy hendrerit as mauris phasellus porta.</p></div></li>
      <li class="news-item"><span class="cal"></span><div><p class="news-date">June 09, 2011</p><p class="news-link">Aenean nonummy hendrerit</p><p class="news-text">Cum sociis natoque penatibus et magnisdis parturient.</p></div></li>
    </ul>
    <span class="more">More News</span>
  </aside>

  <section class="services">
    <h2 class="section-title">WE SPECIALIZES IN AUDITING INFORMATION SECURITY FOR</h2>
    <div class="service-bar">
      <div class="service-tab"><span class="num">1</span>Merchants</div>
      <div class="service-tab"><span class="num">2</span>Retailers</div>
      <div class="service-tab"><span class="num">3</span>Services Providers</div>
    </div>
    <div class="cards">
      <article class="card">
        <h3 class="card-title">AENEAN NONUMMY MAURIS</h3>
        <p class="card-text">Lorem ipsum dolor sit amet sectetuer adipiscing elit aenean nonummy hendrerit maurissellus porta fusce suscipit varius mi.</p>
        <ul class="card-links"><li>Consectetuer adipiscing</li><li>Fusce suscipit varius mi</li><li>Magnis dis parturient</li><li>Nascetur ridiculus mus</li></ul>
        <span class="btn-teal">Read More <i></i></span>
      </article>
      <article class="card">
        <h3 class="card-title">AENEAN NONUMMY MAURIS</h3>
        <p class="card-text">Lorem ipsum dolor sit amet sectetuer adipiscing elit aenean nonummy hendrerit maurissellus porta fusce suscipit varius mi.</p>
        <ul class="card-links"><li>Consectetuer adipiscing</li><li>Fusce suscipit varius mi</li><li>Magnis dis parturient</li><li>Nascetur ridiculus mus</li></ul>
        <span class="btn-teal">Read More <i></i></span>
      </article>
      <article class="card">
        <h3 class="card-title">AENEAN NONUMMY MAURIS</h3>
        <p class="card-text">Lorem ipsum dolor sit amet sectetuer adipiscing elit aenean nonummy hendrerit maurissellus porta fusce suscipit varius mi.</p>
        <ul class="card-links"><li>Consectetuer adipiscing</li><li>Fusce suscipit varius mi</li><li>Magnis dis parturient</li><li>Nascetur ridiculus mus</li></ul>
        <span class="btn-teal">Read More <i></i></span>
      </article>
    </div>
  </section>

  <footer class="footer">
    <span>© Copyright 2011 keystoneassurance.example. All Rights Reserved.</span>
    <nav><span>Site Map</span><span>|</span><span>Privacy Policy</span></nav>
  </footer>

</div>
</body>
</html>
```